Verdano Harvest - Stationery Design Project

We need a stationary for our business. We grow roots and fruits in Central and South America, we import and distribute in FL, USA. We do fresh and frozen products.

Target Market(s)

Small and big supermarkets, wholesalers, traders, distributors, etc

Industry/Entity Type

Business

```html
<!DOCTYPE html>
<html lang="en">
<head>
<meta charset="utf-8">
<title>Verdano Harvest – Letterhead</title>
<link href="https://fonts.googleapis.com/css2?family=Crimson+Pro:wght@400;500&display=swap" rel="stylesheet">
<style>
  :root {
    --backdrop: #54623a;
    --paper: #ffffff;
    --brand-orange: #e8832a;
    --brand-green: #4e5d30;
    --watermark: #eceeed;
  }
  * { box-sizing: border-box; margin: 0; padding: 0; }
  html, body {
    width: 1200px;
    height: 900px;
    overflow: hidden;
    background: var(--backdrop);
  }
  .canvas {
    width: 1200px;
    height: 900px;
    display: flex;
    align-items: center;
    justify-content: center;
  }
  .letterhead {
    position: relative;
    width: 580px;
    height: 820px;
    background: var(--paper);
    box-shadow: 4px 5px 8px rgba(0, 0, 0, 0.35);
    font-family: "Crimson Pro", Georgia, serif;
  }
  .brand {
    position: absolute;
    left: 72px;
    top: 44px;
    display: flex;
    align-items: center;
    gap: 10px;
  }
  .brand-name {
    font-size: 27px;
    font-weight: 500;
    color: var(--brand-orange);
    letter-spacing: 0.5px;
    line-height: 1;
  }
  .brand-dot {
    width: 12px;
    height: 12px;
    border-radius: 50%;
    background: var(--brand-green);
  }
  .contact {
    position: absolute;
    right: 75px;
    top: 44px;
    text-align: right;
    line-height: 1;
  }
  .contact-company {
    font-size: 16px;
    color: var(--brand-orange);
  }
  .contact-address {
    font-size: 18px;
    color: var(--brand-green);
    margin-top: 3px;
  }
  .contact-list {
    list-style: none;
    margin-top: 6px;
  }
  .contact-item {
    display: flex;
    justify-content: flex-end;
    align-items: center;
    gap: 8px;
    font-size: 11px;
    color: var(--brand-green);
    margin-top: 5px;
  }
  .contact-icon {
    width: 12px;
    height: 12px;
    fill: var(--brand-green);
  }
  .watermark {
    position: absolute;
    left: 170px;
    top: 300px;
    width: 240px;
    height: 240px;
    border-radius: 50%;
    background: var(--watermark);
  }
</style>
</head>
<body>
<main class="canvas">
  <article class="letterhead">
    <header class="brand">
      <span class="brand-name">Verdano Harvest</span>
      <span class="brand-dot"></span>
    </header>

    <address class="contact">
      <p class="contact-company">Verdano Harvest Group.</p>
      <p class="contact-address">Address</p>
      <ul class="contact-list">
        <li class="contact-item">Phone
          <svg class="contact-icon" viewBox="0 0 12 12" aria-hidden="true">
            <path d="M1 4.5 C1 2.5 11 2.5 11 4.5 L11 5.5 L8.5 5.5 L8.5 4.5 L3.5 4.5 L3.5 5.5 L1 5.5 Z"/>
            <rect x="2.5" y="6.5" width="7" height="3.5" rx="0.8"/>
          </svg>
        </li>
        <li class="contact-item">Fax
          <svg class="contact-icon" viewBox="0 0 12 12" aria-hidden="true">
            <rect x="2" y="1" width="8" height="10" rx="1.2"/>
          </svg>
        </li>
        <li class="contact-item">Web
          <svg class="contact-icon" viewBox="0 0 12 12" aria-hidden="true">
            <circle cx="6" cy="6" r="5.2"/>
            <path d="M1 6 H11 M6 1 V11" stroke="#fff" stroke-width="0.7"/>
          </svg>
        </li>
      </ul>
    </address>

    <div class="watermark" role="img" aria-label="Faint brand decoration"></div>
  </article>
</main>
</body>
</html>
```